Workvine banner ad for roofing company

We need an ad created for a Workvine banner advertising campaign for a UK based roofing company.

The design should have a large photograph on the background (see attached).
The design should have our Fairmarko rating (5 stars).
There should be a large text header at the top which reads "Your local roofing experts"

The following services should be listed:
- New roofs
- General roof repairs
- Drone surveys
- Single ply roofing
- Steel cladding
- Asbestos removal

The company logo needs to be visible (attached). Also the company telephone number 020 7946 0321 and website www.veldonroofing.com

The advert needs to be horizontal/landscape design. For full spec, please see here: https://business.workvine.com/marketing-solutions/success/ads-guide/single-image-ads

Size required: 1.91:1 - 1200 x 628 pixels

```html
<!DOCTYPE html>
<html lang="en">
<head>
<meta charset="utf-8">
<title>Veldon Roofing – Your Local Roofing Experts</title>
<link href="https://fonts.googleapis.com/css2?family=Roboto:wght@400;500;700;900&display=swap" rel="stylesheet">
<style>
  :root {
    --mint: #a8d6c6;
    --plum: #4b1c44;
    --plum-dark: #3d1838;
    --ink: #111111;
    --gold: #f5a623;
    --white: #ffffff;
    --tone-grass: #7f9566;
    --tone-tree: #5e7448;
    --tone-roof: #b9bcb8;
    --tone-road: #9a9c97;
    --tone-brick: #c99a7c;
    --tone-shade: #6d7564;
  }
  * { margin: 0; padding: 0; box-sizing: border-box; }
  html, body { width: 1200px; height: 628px; overflow: hidden; background: #ffffff; }
  body { font-family: "Roboto", Arial, sans-serif; }

  .banner { position: relative; width: 1200px; height: 628px; overflow: hidden; }

  .aerial-photo {
    position: absolute; inset: 0;
    background:
      radial-gradient(ellipse 160px 220px at 940px 390px, rgba(201,154,124,0.75) 0%, transparent 70%),
      radial-gradient(ellipse 160px 90px at 820px 150px, rgba(201,154,124,0.65) 0%, transparent 70%),
      radial-gradient(ellipse 120px 200px at 710px 440px, rgba(185,188,184,0.9) 0%, transparent 70%),
      radial-gradient(ellipse 130px 160px at 1150px 120px, rgba(210,212,208,0.85) 0%, transparent 70%),
      radial-gradient(ellipse 120px 180px at 1170px 350px, rgba(150,152,160,0.8) 0%, transparent 70%),
      radial-gradient(ellipse 140px 110px at 760px 40px, rgba(154,156,151,0.8) 0%, transparent 70%),
      radial-gradient(ellipse 220px 260px at 830px 330px, rgba(94,116,72,0.55) 0%, transparent 70%),
      radial-gradient(ellipse 200px 200px at 1080px 560px, rgba(94,116,72,0.6) 0%, transparent 70%),
      linear-gradient(160deg, var(--tone-grass) 0%, var(--tone-shade) 40%, var(--tone-road) 70%, var(--tone-grass) 100%);
  }
  .mint-wash {
    position: absolute; inset: 0;
    background: linear-gradient(90deg, rgba(168,214,198,0.97) 0%, rgba(168,214,198,0.93) 36%, rgba(168,214,198,0.6) 48%, rgba(168,214,198,0.2) 58%, rgba(168,214,198,0) 66%);
  }

  .brand { position: absolute; left: 120px; top: 36px; display: flex; align-items: center; gap: 10px; }
  .brand-dot { width: 40px; height: 40px; border-radius: 50%; background: var(--ink); }
  .brand-name { font-size: 36px; font-weight: 700; color: var(--ink); letter-spacing: -0.5px; }

  .headline { position: absolute; left: 67px; top: 114px; padding-left: 22px; border-left: 5px solid var(--plum); }
  .headline-top { display: block; font-size: 53px; font-weight: 500; color: var(--plum); line-height: 58px; letter-spacing: 1px; }
  .headline-main { display: block; font-size: 58px; font-weight: 900; color: var(--ink); line-height: 66px; letter-spacing: 1px; }

  .services { position: absolute; left: 101px; top: 262px; list-style: none; }
  .services li { display: flex; align-items: center; height: 31.2px; font-size: 19px; font-weight: 700; color: #1c1c1c; }
  .services li::before { content: ""; width: 15px; height: 15px; border-radius: 50%; background: var(--plum); margin-right: 8px; }

  .book-now {
    position: absolute; left: 117px; top: 476px; width: 127px; height: 43px;
    border-radius: 22px; background: var(--plum-dark); color: var(--white);
    font-size: 16px; font-weight: 700; display: flex; align-items: center; justify-content: center;
  }

  .contact { position: absolute; top: 563px; display: flex; align-items: center; gap: 6px; }
  .contact.phone { left: 86px; }
  .contact.web { left: 288px; }
  .contact-icon { width: 32px; height: 32px; border-radius: 8px; background: var(--plum); display: flex; align-items: center; justify-content: center; }
  .contact-label { font-size: 12px; font-weight: 700; color: var(--plum); text-transform: uppercase; line-height: 14px; }
  .contact-value { font-size: 17px; font-weight: 700; color: var(--ink); line-height: 20px; }

  .rating {
    position: absolute; left: 987px; top: 467px; width: 213px; height: 50px;
    background: var(--plum-dark); border-radius: 25px 0 0 25px;
    display: flex; align-items: center; justify-content: center; padding-left: 6px;
  }
</style>
</head>
<body>
<main class="banner">
  <div class="aerial-photo" role="img" aria-label="Aerial drone photograph of a residential estate with blocks of flats with grey roofs, lawns, trees, roads and a car park"></div>
  <div class="mint-wash"></div>

  <div class="brand">
    <span class="brand-dot"></span>
    <span class="brand-name">veldonroofing</span>
  </div>

  <h1 class="headline">
    <span class="headline-top">YOUR LOCAL</span>
    <span class="headline-main">ROOFING EXPERTS</span>
  </h1>

  <ul class="services">
    <li>New roofs</li>
    <li>General roof repairs</li>
    <li>Drone surveys</li>
    <li>Single ply roofing</li>
    <li>Steel cladding</li>
    <li>Asbestos removal</li>
  </ul>

  <div class="book-now">BOOK NOW</div>

  <div class="contact phone">
    <span class="contact-icon">
      <svg width="18" height="18" viewBox="0 0 24 24" fill="none" stroke="#fff" stroke-width="2" stroke-linecap="round" stroke-linejoin="round"><path d="M22 16.9v3a2 2 0 0 1-2.2 2 19.8 19.8 0 0 1-8.6-3.1 19.5 19.5 0 0 1-6-6A19.8 19.8 0 0 1 2.1 4.2 2 2 0 0 1 4.1 2h3a2 2 0 0 1 2 1.7c.1.9.4 1.8.7 2.7a2 2 0 0 1-.5 2.1L8 9.8a16 16 0 0 0 6 6l1.3-1.3a2 2 0 0 1 2.1-.4c.9.3 1.8.6 2.7.7a2 2 0 0 1 1.7 2z"/></svg>
    </span>
    <div>
      <div class="contact-label">Telephone number</div>
      <div class="contact-value">020 7946 0321</div>
    </div>
  </div>

  <div class="contact web">
    <span class="contact-icon">
      <svg width="18" height="18" viewBox="0 0 24 24" fill="none" stroke="#fff" stroke-width="2"><circle cx="12" cy="12" r="10"/><path d="M2 12h20M12 2a15 15 0 0 1 0 20M12 2a15 15 0 0 0 0 20"/></svg>
    </span>
    <div>
      <div class="contact-label">Website</div>
      <div class="contact-value">www.veldonroofing.com</div>
    </div>
  </div>

  <div class="rating" aria-label="5 star rating">
    <svg width="180" height="30" viewBox="0 0 180 30">
      <defs><path id="star" d="M15 1.5l4.1 8.6 9.4 1.2-6.9 6.5 1.7 9.3L15 22.6l-8.3 4.5 1.7-9.3-6.9-6.5 9.4-1.2z"/></defs>
      <use href="#star" x="0" fill="#f5a623"/>
      <use href="#star" x="36" fill="#f5a623"/>
      <use href="#star" x="72" fill="#f5a623"/>
      <use href="#star" x="108" fill="#f5a623"/>
      <use href="#star" x="144" fill="#f5a623"/>
    </svg>
  </div>
</main>
</body>
</html>
```